Lindenfall Studio Business cards

Design our business cards and eventually a logo. The company is based in Paris, its activity is the retailing via internet of luxury home furniture (like Vantorelli, Bercasso, fradusi...) Our clients are international andwith a high sense of aesthetics. The design shall communicate wealth and trust with a high quality and aesthetic sense, pure lines Company Name is Lindenfall StudioExplanation of the name: usually people who wants to buy furniture usually go in a showroom. Today they go in showroom to test the furniture and they search for the price on internet, which is a "Lindenfall studio".We will not be a e-commerce site. Our site will be (another project) a presentation site which purpose is to reach qualified prospects. Then everything will be handled by phone, meeting etc.The business card must be professional as we will negotiate with many luxury brands, opportunity to represent them on our site, prices etc.As far as the color are concerned mostly black and whithe or grey. The font of the Lindenfall Studio name shall have some impact.

Target Market(s)

High-end furniture and buyers of luxury goods, international customers, mostly women who handle such projects.
We also deal with professional buyers (hotels as an example) and luxury brands

Contact Information for Business Card

standard format 85x55, lanscape card, square corners will be printed on thick high quality paper (300 or 350g)

Font styles to use
Sans Serif

Colors

Designer to choose colors to be used in the design.

Requirements
Must have
• Must be white, as the paper will be high quality, the paper will enhance the card.
• Name of the brand Lindenfall studio (with specific font which make it very nice looking and catch the attention. similar to Calibri or Calibri
• Name of person (will give you the name later (4 names and position)
• the position of the person
• Mobile phone, e-mail, Physical address 27, rue Caldenois, 75005 Paris, France (courrier only) our web site www.lindenfallstudio-example.fr
• The card must be simple and class
Nice to have
• Font of the address is smaller than the rest,
• Calibri font or similar on recto side with the name of the company which may look similar to the picture inserted in the brief.
• The grey color in the picture inserted is ok for us
Should not have
• Any parallel lines which represent the name of the company
• Any heavy design If you go on internet sites which present the furniture all designs are pure lines and high quality craftsmanship. To have an idea of our targetted client or brand we will be in touch: https://www.casavornetta-example.it/projects/
• Note that the picture added below is what we use, now as mail signature, up to you to have a better design etc.

```html
<!DOCTYPE html>
<html lang="en">
<head>
<meta charset="utf-8">
<title>Lindenfall Studio – Business Card</title>
<link rel="stylesheet" href="https://fonts.googleapis.com/css2?family=Montserrat:wght@500;600;700&display=swap">
<style>
  :root {
    --page-bg: #e6e8eb;
    --card-bg: #ffffff;
    --brand-red: #7a1f26;
    --brand-red-deep: #5e161c;
    --text-grey: #7b7b7d;
    --accent-grey: #a9a9ab;
  }
  html, body {
    margin: 0;
    padding: 0;
    width: 1200px;
    height: 900px;
    overflow: hidden;
    background: var(--page-bg);
    font-family: "Montserrat", Arial, sans-serif;
  }
  .business-card {
    position: absolute;
    left: 150px;
    top: 194px;
    width: 900px;
    height: 512px;
    background: var(--card-bg);
    box-shadow: 0 10px 30px rgba(0,0,0,0.12);
    overflow: hidden;
  }
  .card-curve {
    position: absolute;
    inset: 0;
    width: 900px;
    height: 512px;
  }
  .brand-name {
    position: absolute;
    left: 50px;
    top: 66px;
    margin: 0;
    font-size: 40px;
    font-weight: 700;
    letter-spacing: 1px;
    color: var(--brand-red);
    text-transform: uppercase;
  }
  .person-name {
    position: absolute;
    left: 50px;
    top: 236px;
    margin: 0;
    font-size: 31px;
    font-weight: 700;
    color: var(--brand-red);
    text-transform: uppercase;
  }
  .person-role {
    position: absolute;
    left: 50px;
    top: 277px;
    margin: 0;
    font-size: 25px;
    font-weight: 600;
    color: var(--text-grey);
  }
  .postal-address {
    position: absolute;
    left: 50px;
    top: 322px;
    margin: 0;
    font-style: normal;
    font-size: 24px;
    font-weight: 500;
    line-height: 34px;
    color: var(--text-grey);
  }
  .contact-list {
    position: absolute;
    left: 50px;
    top: 404px;
    margin: 0;
    padding: 0;
    list-style: none;
    font-size: 24px;
    font-weight: 600;
    line-height: 35px;
    color: var(--text-grey);
  }
  .contact-list li {
    display: flex;
    align-items: center;
    gap: 14px;
  }
  .contact-icon {
    width: 22px;
    height: 22px;
    fill: var(--text-grey);
    flex: none;
  }
  .contact-spacer { width: 22px; flex: none; }
</style>
</head>
<body>
  <article class="business-card">
    <svg class="card-curve" viewBox="0 0 900 512" aria-hidden="true">
      <path d="M812 0 C840 130 828 270 740 420" fill="none" stroke="var(--accent-grey)" stroke-width="12" stroke-linecap="round"/>
      <path d="M848 0 L900 0 L900 512 L626 512 C780 420 862 250 848 0 Z" fill="var(--brand-red)"/>
    </svg>

    <h1 class="brand-name">Lindenfall Studio</h1>

    <h2 class="person-name">Mael Darcourt</h2>
    <p class="person-role">President and Co-Founder</p>

    <address class="postal-address">
      27, rue Caldenois<br>
      75005 Paris, France
    </address>

    <ul class="contact-list">
      <li>
        <svg class="contact-icon" viewBox="0 0 24 24" aria-hidden="true">
          <path d="M6.6 10.8a15.1 15.1 0 0 0 6.6 6.6l2.2-2.2a1 1 0 0 1 1-.25 11.4 11.4 0 0 0 3.6.57 1 1 0 0 1 1 1V20a1 1 0 0 1-1 1A17 17 0 0 1 3 4a1 1 0 0 1 1-1h3.5a1 1 0 0 1 1 1c0 1.25.2 2.45.57 3.57a1 1 0 0 1-.25 1z"/>
        </svg>
        <span>+33612047385</span>
      </li>
      <li>
        <span class="contact-spacer"></span>
        <span>www.lindenfallstudio-example.fr</span>
      </li>
    </ul>
  </article>
</body>
</html>
```